Flyer Design Project

I am opening a yoga studio called Willowmere Yoga .Pilates. Fitness
and require a flyer that will be letterbox dropped. It will two sided - DL size.100mm × 210mm

The studio will offer Vinyasa Flow Yoga and Mat Pilates classes. We aim to enable people to lead healthier, happier lives through improved strength, flexibility and general well being that regular yoga and pilates practice offers.

We offer group classes, private and semi private sessions in yoga and pilates.

it must have the logo on it- I have uploaded the logo in two versions - not sure what will look the best.

pick up one of the colours from the logo as the background colour.

Side one:
Simple and clean with one side showing logo and address details, website and with simple intro about studio (if it fits)

Location: 1st Floor, 17 Larkspur Parade, Tindale, 3286
phone: 0428 596143
www.willowmeretindale.com.au

OPENING OCTOBER

other side - class descriptions and intro offer for new clients
$20 for 7 days of classes
$99 for 1 month unlimited.

Class descriptions:
Vinyasa Flow yoga: A class that flows from pose to pose integrating breath, alignment, strength and power. All levels are catered for in a warm room heated to around 26 degrees. You will leave feeling inspired, empowered and energised.

Mat Pilates: A strong, challenging class integrating the key principles of pilates: concentration, control, centring, precision, flowing movement and breath. Using the core as a focus to develop these principles you will be hooked on the physical freedom you experience post workout:improved strength, flexibility and vitality that pilates offers.

Private and semi Private tuition available.

Target Market(s)

mainly women, athletic, 35-55 age, middle class, well educated

Industry/Entity Type

Fitness

Requirements
Must have
• 2 pages
the logo

Should not have
• no pics

```html
<!DOCTYPE html>
<html lang="en">
<head>
<meta charset="utf-8">
<title>Willowmere Yoga .Pilates. Fitness – DL Flyer</title>
<link rel="stylesheet" href="https://fonts.googleapis.com/css2?family=Montserrat:wght@400;700;800&family=Poppins:wght@300;400&family=Open+Sans:wght@400;600&family=Lora:ital@1&display=swap">
<style>
  :root {
    --page-bg: #ece7df;
    --ink: #0d0b09;
    --orange: #f29a1f;
    --orange-deep: #d8761a;
    --gold: #ffc23a;
    --sun-bright: #ffd25a;
    --sun-mid: #f08a1c;
    --sun-dark: #6a2a08;
    --cream: #f3ece1;
    --text-light: #f2e6d4;
    --logo-ink: #2c4f86;
  }
  * { box-sizing: border-box; margin: 0; padding: 0; }
  html, body { width: 1200px; height: 1000px; overflow: hidden; }
  body { background: var(--page-bg); font-family: "Open Sans", sans-serif; position: relative; }

  .flyer {
    position: absolute; top: 100px; width: 380px; height: 800px;
    overflow: hidden; background: var(--ink);
    box-shadow: 0 10px 30px rgba(0,0,0,.25);
  }
  .flyer--offer { left: 170px; }
  .flyer--intro { left: 650px; }

  .photo { position: absolute; left: 0; right: 0; }
  .flyer--offer .photo {
    top: 0; height: 400px;
    background: radial-gradient(circle at 60% 70%, var(--sun-bright) 0%, var(--sun-mid) 35%, var(--sun-dark) 85%);
  }
  .flyer--offer .photo::after {
    content: ""; position: absolute; left: 0; right: 0; bottom: 0; height: 90px;
    background: linear-gradient(to bottom, rgba(13,11,9,0), var(--ink));
  }
  .flyer--intro .photo {
    top: 0; bottom: 0;
    background:
      linear-gradient(to bottom, rgba(13,11,9,0) 50%, var(--ink) 88%),
      linear-gradient(to bottom, #9b4a12 0%, var(--sun-mid) 24%, var(--sun-bright) 36%, #7a300a 48%, #2a1006 60%, #1a0a04 100%);
  }

  .logo-box {
    position: absolute; top: 26px; right: 26px; width: 150px; height: 118px;
    background: var(--cream);
    display: flex; flex-direction: column; align-items: center; justify-content: center; gap: 8px;
    padding: 10px;
  }
  .logo-box__dot { width: 30px; height: 30px; border-radius: 50%; background: var(--orange); }
  .logo-box__name {
    font-family: "Montserrat", sans-serif; font-weight: 700; font-size: 12px;
    color: var(--logo-ink); text-align: center; line-height: 1.3; text-transform: uppercase;
  }

  .price-panel {
    position: absolute; top: 160px; right: 26px; width: 150px; height: 220px;
    background: rgba(40,20,6,.55); color: #fff; text-align: center;
    display: flex; flex-direction: column; justify-content: center; padding: 0 10px;
  }
  .price { font-family: "Poppins", sans-serif; font-weight: 300; font-size: 52px; color: var(--gold); line-height: 1; }
  .price sup { font-size: 24px; vertical-align: top; }
  .price-note { font-family: "Montserrat", sans-serif; font-weight: 700; font-size: 9px; letter-spacing: .3px; margin-top: 4px; }
  .price-rule { height: 1px; background: rgba(255,255,255,.6); margin: 18px 10px; }

  .classes { position: absolute; left: 26px; right: 26px; top: 410px; color: var(--text-light); }
  .classes__title {
    font-family: "Montserrat", sans-serif; font-weight: 800; font-size: 13px;
    color: var(--orange); text-transform: uppercase; letter-spacing: .5px; margin-bottom: 6px;
  }
  .classes__text { font-size: 11px; line-height: 1.55; margin-bottom: 16px; }

  .band {
    position: absolute; left: 0; right: 0; bottom: 0; height: 48px;
    background: linear-gradient(to right, var(--orange-deep), var(--orange));
    display: flex; align-items: center; justify-content: center;
    font-family: "Montserrat", sans-serif; font-weight: 700; font-size: 11px;
    color: var(--ink); text-transform: uppercase; letter-spacing: .4px;
  }

  .tagline {
    position: absolute; right: 30px; top: 470px; width: 230px;
    font-family: "Lora", serif; font-style: italic; font-size: 19px; line-height: 1.3;
    color: var(--orange); text-align: right;
  }
  .contact { position: absolute; left: 26px; right: 26px; bottom: 62px; }
  .contact__opening {
    font-family: "Montserrat", sans-serif; font-weight: 800; font-size: 13px;
    color: var(--gold); text-transform: uppercase; letter-spacing: 2px; margin-bottom: 10px;
  }
  .contact__location {
    font-family: "Montserrat", sans-serif; font-weight: 700; font-size: 9.5px;
    color: var(--text-light); text-transform: uppercase; letter-spacing: .3px; margin-bottom: 6px;
    white-space: nowrap;
  }
  .contact__phone {
    font-family: "Montserrat", sans-serif; font-weight: 800; font-size: 26px;
    color: var(--orange); letter-spacing: .3px; text-transform: uppercase;
    white-space: nowrap; line-height: 1.1;
  }
  .band--web { font-size: 13px; letter-spacing: 1.5px; }
</style>
</head>
<body>

  <section class="flyer flyer--offer">
    <div class="photo" role="img" aria-label="Sunset sky with a silhouette of a woman in tree pose on a rocky ledge"></div>
    <div class="logo-box">
      <span class="logo-box__dot"></span>
      <span class="logo-box__name">Willowmere Yoga .Pilates. Fitness</span>
    </div>
    <div class="price-panel">
      <div class="price"><sup>$</sup>20</div>
      <div class="price-note">FOR 7 DAYS OF CLASSES</div>
      <div class="price-rule"></div>
      <div class="price"><sup>$</sup>99</div>
      <div class="price-note">FOR 1 MONTH UNLIMITED</div>
    </div>
    <div class="classes">
      <h2 class="classes__title">Class Descriptions:</h2>
      <p class="classes__text">Vinyasa Flow yoga: A class that flows from pose to pose integrating breath, alignment, strength and power. All levels are catered for in a warm room heated to around 26 degrees. You will leave feeling inspired, empowered and energised.</p>
      <h2 class="classes__title">Mat Pilates:</h2>
      <p class="classes__text">A strong, challenging class integrating the key principles of pilates: concentration, control, centring, precision, flowing movement and breath. Using the core as a focus to develop these principles you will be hooked on the physical freedom you experience post workout: improved strength, flexibility and vitality that pilates offers.</p>
    </div>
    <div class="band">Private and semi private tuition available</div>
  </section>

  <section class="flyer flyer--intro">
    <div class="photo" role="img" aria-label="Silhouette of a woman seated in meditation facing an ocean sunset"></div>
    <div class="logo-box">
      <span class="logo-box__dot"></span>
      <span class="logo-box__name">Willowmere Yoga .Pilates. Fitness</span>
    </div>
    <p class="tagline">…a sacred space for opening your heart and your yoga practice</p>
    <div class="contact">
      <p class="contact__opening">Opening October</p>
      <p class="contact__location">Location: 1st Floor, 17 Larkspur Parade, Tindale, 3286</p>
      <p class="contact__phone">Phone: 0428 596143</p>
    </div>
    <div class="band band--web">www.willowmeretindale.com.au</div>
  </section>

</body>
</html>
```